BrivoPeak Business Card Design Project

We are looking for a modern, clean business card design for our new company. We are a consulting firm focused on the financial services market providing management and IT consulting to banks, insurance companies, etc. Please include our company logo and company contact information from the attached file in the design. Two versions of the logo are attached, either version is acceptable. Logos are available in other file formats if needed. We would like to include the contact information for both our UK and US offices as well as the following information for each individual card holder: Name, position/title, address, phone number and e-mail address.
Updates
Project Deadline Extended
Reason: A last minute trip over seas has prevented us from finalizing the decision. A decision will be made this week. We apologize for the inconvenience.
Industry/Entity Type
Business
Contact Information for Business Card
Company logo.
Company locations and phone numbers for both the US and UK offices.
Company URL.
Cardholder Name
Cardholder Position/title
Cardholder Address
Cardholder Phone Number
Cardholder e-mail Address
Look and feel
Each slider illustrates characteristics of the customer's brand and the style your logo design should communicate.

```html
<!DOCTYPE html>
<html lang="en">
<head>
<meta charset="utf-8">
<title>BrivoPeak Partners – Business Card</title>
<link href="https://fonts.googleapis.com/css2?family=Arimo:wght@400;700&display=swap" rel="stylesheet">
<style>
  :root {
    --navy: #253a62;
    --navy-deep: #1f3258;
    --grey: #6f6f73;
    --grey-tab: #7a7a7e;
    --ink: #3d3d40;
    --paper: #ffffff;
    --backdrop: #ecebe8;
  }
  * { box-sizing: border-box; margin: 0; padding: 0; }
  html, body { width: 1200px; height: 1023px; overflow: hidden; }
  body {
    background: var(--backdrop);
    font-family: "Arimo", Arial, sans-serif;
    position: relative;
  }
  .card {
    position: absolute;
    width: 600px;
    height: 343px;
    border-radius: 3px;
    box-shadow: 0 6px 18px rgba(0,0,0,0.18);
    overflow: hidden;
  }
  /* Front */
  .card--front { left: 60px; top: 90px; background: var(--paper); }
  .brand {
    position: absolute; left: 46px; top: 58px;
    display: flex; align-items: center; gap: 12px;
  }
  .brand__square { width: 22px; height: 22px; background: var(--navy); }
  .brand__name {
    font-weight: 700; font-size: 30px; color: var(--navy); letter-spacing: 0.2px;
  }
  .holder { position: absolute; left: 46px; top: 150px; }
  .holder__name { font-size: 19px; color: var(--navy); font-weight: 700; }
  .holder__title { font-size: 14px; color: var(--ink); margin-top: 4px; }
  .address { font-size: 13.5px; line-height: 1.35; color: var(--ink); }
  .address--uk { position: absolute; left: 46px; top: 222px; }
  .address--us { position: absolute; right: 40px; top: 40px; text-align: right; }
  .contacts {
    position: absolute; right: 40px; top: 150px;
    list-style: none; font-size: 13.5px; line-height: 1.5; color: var(--ink);
  }
  .contacts li { display: flex; justify-content: flex-end; align-items: center; gap: 8px; }
  .contacts svg { width: 13px; height: 13px; flex: none; }
  .front-band {
    position: absolute; left: 0; right: 0; bottom: 0; height: 14px; background: var(--navy);
  }
  .front-tab {
    position: absolute; left: 150px; bottom: 10px; width: 62px; height: 14px;
    background: var(--navy); border-radius: 5px 5px 0 0;
  }
  .web-tab {
    position: absolute; right: 0; bottom: 14px; width: 220px; height: 36px;
    background: var(--grey-tab); color: #fff; font-size: 13px;
    display: flex; align-items: center; justify-content: center;
  }
  /* Back */
  .card--back {
    left: 540px; top: 580px;
    background: linear-gradient(135deg, var(--navy) 0%, var(--navy-deep) 100%);
    display: flex; align-items: center; justify-content: center; gap: 14px;
  }
  .card--back .brand__square { width: 28px; height: 28px; background: #fff; }
  .card--back .brand__name { color: #fff; font-size: 40px; }
</style>
</head>
<body>
  <section class="card card--front" aria-label="Business card front">
    <div class="brand">
      <span class="brand__square"></span>
      <span class="brand__name">BrivoPeak Partners</span>
    </div>
    <div class="holder">
      <p class="holder__name">Daniel Harper</p>
      <p class="holder__title">Founder</p>
    </div>
    <address class="address address--uk">
      14-16 Harlow Street<br>London<br>N4 2QR Great Britain
    </address>
    <address class="address address--us">
      418 N Maple Ave, Suite 210-114<br>Lakeview UT 84120<br>United States
    </address>
    <ul class="contacts">
      <li>(555) 014-2270 US
        <svg viewBox="0 0 14 14"><rect width="14" height="14" rx="2" fill="#5b6f96"/><rect x="4.5" y="2.5" width="5" height="9" rx="1" fill="#fff"/></svg>
      </li>
      <li>+44 7700 900418 UK
        <svg viewBox="0 0 14 14"><rect width="14" height="14" rx="2" fill="#5b6f96"/><rect x="4.5" y="2.5" width="5" height="9" rx="1" fill="#fff"/></svg>
      </li>
      <li>info@brivopeakpartners.com
        <svg viewBox="0 0 14 14"><rect width="14" height="14" rx="2" fill="#5b6f96"/><rect x="2.5" y="4" width="9" height="6" fill="#fff"/><path d="M2.5 4 7 7.5 11.5 4" stroke="#5b6f96" fill="none"/></svg>
      </li>
    </ul>
    <div class="web-tab">www.brivopeakpartners.com</div>
    <div class="front-tab"></div>
    <div class="front-band"></div>
  </section>

  <section class="card card--back" aria-label="Business card back">
    <span class="brand__square"></span>
    <span class="brand__name">BrivoPeak Partners</span>
  </section>
</body>
</html>
```